Business Card design for amazing new Dental Office

Please read this brief closely!

Our client is a modern new dental office/
They love their new logo.
Now it's time to create a business card for them.

It should be a two sided card:
Side one should have the logo and name and maybe a color background or design.
Side two should have all the contact information which is here:

Marcus Pellow, D.D.S
General and Cosmetic Dentistry
4178 W. Orchard Lane
Ventura, CA 93017
(805) 219-4862
drmarc@bluefernsmiles.example
www.bluefernsmiles.example

Feel free to arrange that info as you like and to style both sides of the card according to your creativity. This is a chance for you to show your design skills!

Client is open to font choices and is looking for a style that is amazing and premium. Colors can be selected from the logo, or any variation of those.

You will not win this contest with a less than beautiful card design so please feel free to make multiple submissions.

Logo files attached and please message me with any questions.
Thanks!

Target Market(s)

Families and Professionals seeking dental services

Industry/Entity Type

Dental

Contact Information for Business Card

Logo, style, contact info as per the brief

Font styles to use
Sans Serif

Requirements
Must have
• Client's logo and contact details as per brief
Nice to have
• Unique style reflecting high end dental clinic near the beach
Should not have
• Must not look like a template

```html
<!DOCTYPE html>
<html lang="en">
<head>
<meta charset="utf-8">
<title>Blue Fern Smiles – Business Card</title>
<link rel="stylesheet" href="https://fonts.googleapis.com/css2?family=Lato:wght@300;400&display=swap">
<style>
  :root {
    --backdrop: #a4a5a7;
    --card-light: #ffffff;
    --card-dark: #232325;
    --brand-blue: #3aa8e0;
    --text-grey: #555759;
    --wordmark-grey: #8a8c8e;
    --wordmark-light: #d6d6d6;
    --accent-gold: #e0a65a;
    --sun-gold: #e2b54a;
  }
  * { margin: 0; padding: 0; box-sizing: border-box; }
  html, body { width: 1200px; height: 1200px; overflow: hidden; }
  body {
    background: var(--backdrop);
    font-family: "Lato", sans-serif;
    position: relative;
  }
  .card {
    position: absolute;
    left: 223px;
    width: 754px;
    height: 463px;
  }
  .card-front {
    top: 105px;
    background: var(--card-light);
    border-radius: 0 40px 0 40px;
  }
  .card-back {
    top: 629px;
    background: radial-gradient(circle at 30% 20%, #2b2b2d 0%, var(--card-dark) 60%);
    border-radius: 40px 0 40px 0;
  }

  /* brand block */
  .brand { position: absolute; text-align: center; font-weight: 300; }
  .brand-dot { display: block; margin: 0 auto; border-radius: 50%; background: var(--sun-gold); }
  .brand-name { display: block; white-space: nowrap; }
  .brand-sub { display: block; white-space: nowrap; }

  .card-front .brand { left: 80px; top: 48px; width: 240px; color: var(--wordmark-grey); }
  .card-front .brand-dot { width: 64px; height: 64px; margin-bottom: 30px; }
  .card-front .brand-name { font-size: 31px; letter-spacing: 2px; line-height: 1; }
  .card-front .brand-sub { font-size: 16px; letter-spacing: 10px; margin-top: 12px; padding-left: 10px; }

  .card-back .brand { left: 0; right: 0; top: 110px; color: var(--wordmark-light); }
  .card-back .brand-dot { width: 82px; height: 82px; margin-bottom: 46px; }
  .card-back .brand-name { font-size: 44px; letter-spacing: 3px; line-height: 1; }
  .card-back .brand-sub { font-size: 22px; letter-spacing: 17px; margin-top: 18px; padding-left: 17px; }

  /* practitioner */
  .practitioner { position: absolute; right: 47px; top: 218px; text-align: right; }
  .practitioner-name { font-size: 31px; font-weight: 400; color: var(--brand-blue); line-height: 1.1; }
  .practitioner-role { font-size: 20px; font-weight: 400; color: var(--text-grey); margin-top: 4px; }

  .divider { position: absolute; left: 46px; right: 47px; top: 297px; height: 2px; background: var(--accent-gold); }

  /* contact */
  .contact-list { position: absolute; left: 46px; top: 326px; list-style: none; }
  .contact-item {
    display: flex; align-items: center; gap: 14px;
    font-size: 21px; font-weight: 400; color: var(--text-grey);
    height: 31.5px;
  }
  .contact-icon { width: 21px; height: 21px; flex: none; }

  .address { position: absolute; right: 47px; top: 330px; text-align: right; color: var(--text-grey); font-size: 21px; line-height: 28px; }
  .address-pin { width: 18px; height: 24px; display: block; margin-left: auto; margin-bottom: 2px; margin-right: 2px; }
</style>
</head>
<body>

<section class="card card-front">
  <div class="brand">
    <span class="brand-dot"></span>
    <span class="brand-name">BLUE FERN</span>
    <span class="brand-sub">SMILES</span>
  </div>

  <div class="practitioner">
    <p class="practitioner-name">Marcus Pellow, D.D.S</p>
    <p class="practitioner-role">General and Cosmetic Dentistry</p>
  </div>

  <div class="divider"></div>

  <ul class="contact-list">
    <li class="contact-item">
      <svg class="contact-icon" viewBox="0 0 24 24" aria-hidden="true"><path fill="#3aa8e0" d="M6.6 2.5l3 3.6c.4.5.4 1.2 0 1.7L8 9.6c1.2 2.6 3.6 5 6.4 6.4l1.8-1.6c.5-.4 1.2-.4 1.7 0l3.6 3c.5.4.6 1.2.1 1.7l-1.9 2.1c-.6.6-1.5.9-2.4.7C9.5 20.3 3.7 14.5 2.1 6.7c-.2-.9.1-1.8.7-2.4L4.9 2.4c.5-.5 1.3-.4 1.7.1z"/></svg>
      <span>(805) 219-4862</span>
    </li>
    <li class="contact-item">
      <svg class="contact-icon" viewBox="0 0 24 24" aria-hidden="true"><rect x="1" y="4" width="19" height="13" rx="1.5" fill="#3aa8e0"/><path d="M2 5l8.5 6.5L19 5" fill="none" stroke="#fff" stroke-width="1.6"/><circle cx="18.5" cy="18" r="5" fill="#3aa8e0" stroke="#fff" stroke-width="1.2"/><path d="M16.3 18l1.6 1.6 2.8-3" fill="none" stroke="#fff" stroke-width="1.5"/></svg>
      <span>drmarc@bluefernsmiles.example</span>
    </li>
    <li class="contact-item">
      <svg class="contact-icon" viewBox="0 0 24 24" aria-hidden="true"><g fill="none" stroke="#3aa8e0" stroke-width="1.5"><circle cx="12" cy="12" r="10"/><ellipse cx="12" cy="12" rx="4.5" ry="10"/><path d="M2 12h20M4 6.5h16M4 17.5h16"/></g></svg>
      <span>www.bluefernsmiles.example</span>
    </li>
  </ul>

  <address class="address" style="font-style:normal">
    <svg class="address-pin" viewBox="0 0 18 24" aria-hidden="true"><path fill="#3aa8e0" d="M9 0C4 0 0 4 0 9c0 6.5 9 15 9 15s9-8.5 9-15c0-5-4-9-9-9zm0 12.5A3.5 3.5 0 1 1 9 5.5a3.5 3.5 0 0 1 0 7z"/></svg>
    4178 W. Orchard Lane<br>
    Ventura, CA 93017
  </address>
</section>

<section class="card card-back">
  <div class="brand">
    <span class="brand-dot"></span>
    <span class="brand-name">BLUE FERN</span>
    <span class="brand-sub">SMILES</span>
  </div>
</section>

</body>
</html>
```